Pediatric Dentist Business Card

I need a business card designed for a dentist who works exclusively with children.
We prefer designs that are out of ordiary that is fun and interesting to kids.

there is no logo since this is a dentists office. The name of the doctor is "Tavor Kesh" if you want to get creative with that.

Target Market(s)

Kids

Industry/Entity Type

Business

Contact Information for Business Card

Anythings that is creative

Colors

Designer to choose colors to be used in the design.

```html
<!DOCTYPE html>
<html lang="en">
<head>
<meta charset="utf-8">
<title>Tavor Kesh – Pediatric Dentist Business Card</title>
<link href="https://fonts.googleapis.com/css2?family=Amatic+SC:wght@400;700&family=Gochi+Hand&family=Quicksand:wght@400&display=swap" rel="stylesheet">
<style>
  :root {
    --teal: #1ec8bb;
    --teal-light: #5fd9cf;
    --white: #ffffff;
    --paper-bg: #eef2f1;
    --pink: #f27aa8;
    --orange: #f7a233;
    --green: #8cc63f;
    --yellow: #f5d327;
    --purple: #b07ad8;
  }
  * { box-sizing: border-box; margin: 0; padding: 0; }
  html, body {
    width: 1200px; height: 800px; overflow: hidden;
    background: var(--paper-bg);
  }
  .canvas {
    position: relative; width: 1200px; height: 800px;
    display: flex; justify-content: center; align-items: center; gap: 70px;
  }
  .card {
    position: relative; width: 320px; height: 560px; overflow: hidden;
    box-shadow: 0 8px 24px rgba(0,0,0,0.12);
  }

  .doctor-name {
    font-family: "Amatic SC", cursive;
    font-weight: 400; font-size: 58px; line-height: 1;
    letter-spacing: 1px; white-space: nowrap;
  }
  .specialty {
    font-family: "Gochi Hand", cursive;
    font-size: 22px; line-height: 1; letter-spacing: 1px; white-space: nowrap;
  }
  .specialty .c1 { color: var(--yellow); }
  .specialty .c2 { color: var(--pink); }
  .specialty .c3 { color: var(--orange); }
  .specialty .c4 { color: var(--green); }
  .specialty .c5 { color: var(--purple); }

  /* Contact side */
  .card--contact { background: var(--white); }
  .card--contact .side-band {
    position: absolute; left: 0; top: 0; bottom: 0; width: 68px;
    background: var(--teal);
  }
  .card--contact .heading {
    position: absolute; left: 90px; top: 108px;
  }
  .card--contact .doctor-name { color: var(--teal); }
  .card--contact .specialty { margin-top: 2px; }
  .contact-list {
    position: absolute; left: 28px; right: 18px; top: 224px;
    list-style: none;
  }
  .contact-item {
    display: flex; align-items: center; height: 36px;
    border-bottom: 2px dotted var(--teal);
  }
  .contact-item .icon {
    width: 40px; display: flex; justify-content: center;
  }
  .contact-item .icon svg { width: 14px; height: 14px; fill: var(--white); }
  .contact-item .value {
    margin-left: 24px;
    font-family: "Quicksand", sans-serif; font-size: 15px;
    color: var(--teal);
  }

  /* Front side */
  .card--front {
    background: repeating-linear-gradient(90deg,
      var(--teal) 0 36px, var(--teal-light) 36px 72px);
  }
  .card--front .heading {
    position: absolute; left: 0; right: 0; top: 54px; text-align: center;
  }
  .card--front .doctor-name { color: var(--white); font-size: 66px; }
  .card--front .specialty { color: var(--white); margin-top: 4px; }
  .illustration {
    position: absolute; left: 0; right: 0; top: 240px; bottom: 0;
    background: linear-gradient(160deg,
      rgba(255,255,255,0) 0%, rgba(165,214,74,0.45) 50%, rgba(255,255,255,0.55) 100%);
  }
</style>
</head>
<body>
<main class="canvas">

  <article class="card card--contact">
    <div class="side-band"></div>
    <header class="heading">
      <h1 class="doctor-name">Tavor Kesh</h1>
      <p class="specialty"><span class="c1">p</span><span class="c2">e</span><span class="c3">d</span><span class="c4">i</span><span class="c5">a</span><span class="c2">t</span><span class="c1">r</span><span class="c3">i</span><span class="c4">c</span> <span class="c5">d</span><span class="c3">e</span><span class="c2">n</span><span class="c1">t</span><span class="c4">i</span><span class="c5">s</span><span class="c2">t</span></p>
    </header>
    <ul class="contact-list">
      <li class="contact-item">
        <span class="icon"><svg viewBox="0 0 14 14"><path d="M4 0h6a1 1 0 0 1 1 1v12a1 1 0 0 1-1 1H4a1 1 0 0 1-1-1V1a1 1 0 0 1 1-1zm.5 1.5v9.5h5V1.5z"/></svg></span>
        <span class="value">123.456789</span>
      </li>
      <li class="contact-item">
        <span class="icon"><svg viewBox="0 0 14 14"><path d="M7 0a5 5 0 0 1 5 5c0 3.5-5 9-5 9S2 8.5 2 5a5 5 0 0 1 5-5zm0 3a2 2 0 1 0 0 4 2 2 0 0 0 0-4z"/></svg></span>
        <span class="value">address lorem ipsum 2</span>
      </li>
      <li class="contact-item">
        <span class="icon"><svg viewBox="0 0 14 14"><path d="M0 3h14v9H0zm1 1v.4l6 4 6-4V4z"/></svg></span>
        <span class="value">info@domainname.com</span>
      </li>
      <li class="contact-item">
        <span class="icon"><svg viewBox="0 0 14 14"><path d="M7 13S0 8.5 0 4.2A3.6 3.6 0 0 1 7 3a3.6 3.6 0 0 1 7 1.2C14 8.5 7 13 7 13z"/></svg></span>
        <span class="value">www.domainname.com</span>
      </li>
    </ul>
  </article>

  <article class="card card--front">
    <header class="heading">
      <h2 class="doctor-name">Tavor Kesh</h2>
      <p class="specialty">pediatric dentist</p>
    </header>
    <div class="illustration" role="img" aria-label="Playful illustration area"></div>
  </article>

</main>
</body>
</html>
```